Fatigued and Overloaded by COVID Messages? We need original illustrations to show that.

Everywhere you look there are messages about COVID. That is leading many people to feel fatigued and overloaded by the messages.

We surveyed U.S. adults March 20th - 24th, 2020 and measured message fatigue, information overload, perceived repetition, and perceived exaggeration. Here is how participants responded:

When it comes to coronavirus . . .
55% feel exhausted by all the messages.
54% feel overloaded by the amount of information.
51% feel that the messages are repetitive.
47% feel like messages exaggerate how bad it is.

In other words, almost half of U.S. adults show signs of message fatigue, information overload, perceived message repetition, and perceived message exaggeration.

We will continue to survey 400 adults every week for the next 16 weeks. Each time we will measure message fatigue, information overload, perceived repetition, and perceived exaggeration. We expect that it will increase over time.

What are we looking for? We need innovative and original illustrations that attempt to communicate these findings. The illustrations would visualize message fatigue, information overload, perceived message repetition, and perceived message exaggeration.

What sort of visual are we looking for? Our preference is for an original illustration (or set of illustrations). Our preference is for creative and powerful illustrations, but we are also open to the creative and well-executed infographics.

We need these images fast . We will award monetary prizes to the 3 best designs. If we like more than that, then we might purchase more (e.g., in past contests, we have purchased as many as 30 designs).

What we will need:
(1) The illustrations must be original and we will need the photoshop and/or illustrator files for all artwork. (By original, we mean that the illustrations are 100% created by you. Our organization requires that we utilize only original illustrated work. We have had issues with free imagery being pirated and reposted as free. We sidestep that issue by just having everything created.)

(2) The illustration should say, somewhere: "Based on a survey of 400 U.S. adults conducted March 20 - 24th, 2020."

(3) We will have almost 4 months worth of data by the time this is done. In other words, the illustrations might be able to help us present that weekly data.

(4) We have conducted other Artvendo projects. It might be helpful to examine designs we liked in the past. For example, here is another COVID project we just finished:

https://jobs.artvendo-example.com/job/5162048

Target Market(s)

U.S. adults

Requirements
Must have
• Original illustrations. Mobile friendly design. People will view this on their smartphones.
Nice to have
• A design that we can use to communicate the data across time.

```html
<!DOCTYPE html>
<html lang="en">
<head>
<meta charset="utf-8">
<title>When it comes to coronavirus</title>
<link rel="stylesheet" href="https://fonts.googleapis.com/css2?family=Fredoka:wght@600;700&family=Cabin:wght@500;600&display=swap">
<style>
  :root {
    --ink: #1c1c2e;
    --navy: #1f1a66;
    --purple: #662a8e;
    --orange: #f9ae3b;
    --orange-art: #f7b043;
    --tan: #dcc3a5;
    --tan-art: #e0c7a9;
    --magenta: #a10058;
    --magenta-art: #a7045c;
    --lime: #dbe021;
    --lime-art: #dde229;
    --bar-track: #e4e4e4;
    --bar-fill: #4f8ff2;
    --white: #ffffff;
  }
  * { margin: 0; padding: 0; box-sizing: border-box; }
  html, body { width: 676px; height: 1200px; overflow: hidden; }
  body {
    position: relative;
    background: linear-gradient(180deg, #ffffff 0%, #eef1f6 12%, #ffffff 84%, #cfe3c4 100%);
    font-family: "Cabin", sans-serif;
    color: var(--ink);
  }
  .survey-note {
    position: absolute; top: 36px; left: 0; width: 100%;
    text-align: center; font-family: "Fredoka", sans-serif; font-weight: 700;
    font-size: 17px; line-height: 21px; color: var(--navy); text-transform: uppercase;
  }
  .lead-pill {
    position: absolute; top: 101px; left: 32px; width: 616px; height: 54px;
    background: var(--purple); border-radius: 27px;
    color: var(--white); font-family: "Fredoka", sans-serif; font-weight: 700;
    font-size: 33px; line-height: 54px; text-align: center; letter-spacing: 0.3px;
  }
  .band { position: absolute; left: 0; width: 676px; }
  .band--exhausted { top: 164px; height: 209px; background: var(--orange); border-radius: 44px 44px 0 0; }
  .band--overloaded { top: 372px; height: 227px; background: var(--tan); }
  .band--repetitive { top: 598px; height: 217px; background: var(--magenta); color: var(--white); }
  .band--exaggerated { top: 815px; height: 201px; background: var(--lime); }
  .illustration {
    position: absolute; left: 61px; width: 202px;
    box-shadow: 3px 5px 8px rgba(0,0,0,0.18);
  }
  .band--exhausted .illustration { top: 26px; height: 168px; background: var(--orange-art); }
  .band--overloaded .illustration { top: 29px; height: 182px; background: var(--tan-art); }
  .band--repetitive .illustration { top: 20px; height: 178px; background: var(--magenta-art); }
  .band--exaggerated .illustration { top: 11px; height: 180px; background: var(--lime-art); }
  .stat-bar {
    position: absolute; left: 288px; width: 313px; height: 72px; background: var(--bar-track);
  }
  .stat-fill {
    position: absolute; left: 0; top: 0; height: 72px; background: var(--bar-fill);
    border-radius: 0 36px 36px 0;
  }
  .stat-value {
    position: absolute; left: 14px; top: 0; line-height: 72px;
    font-family: "Fredoka", sans-serif; font-weight: 700; font-size: 54px; color: var(--white);
  }
  .stat-label {
    position: absolute; left: 290px; width: 370px;
    font-weight: 500; font-size: 32px; line-height: 42px; letter-spacing: 0.6px;
  }
  .band--exhausted .stat-bar { top: 36px; }
  .band--exhausted .stat-label { top: 112px; left: 294px; }
  .band--overloaded .stat-bar { top: 28px; }
  .band--overloaded .stat-label { top: 112px; }
  .band--repetitive .stat-bar { top: 25px; }
  .band--repetitive .stat-label { top: 108px; }
  .band--exaggerated .stat-bar { top: 23px; }
  .band--exaggerated .stat-label { top: 103px; left: 288px; }
  .summary {
    position: absolute; top: 1054px; left: 40px; width: 596px;
    text-align: center; font-size: 19.5px; line-height: 28px; letter-spacing: 0.3px;
  }
</style>
</head>
<body>
  <p class="survey-note">"Based on a survey of 400 U.S. adults<br>conducted March 20 - 24th, 2020."</p>
  <h1 class="lead-pill">When it comes to coronavirus . . .</h1>

  <section class="band band--exhausted">
    <div class="illustration" role="img" aria-label="Illustration of a tired person slumped beside speech bubbles filled with virus messages"></div>
    <div class="stat-bar"><div class="stat-fill" style="width:177px"></div><span class="stat-value">55%</span></div>
    <p class="stat-label">Feel exhausted by all<br>the messages.</p>
  </section>

  <section class="band band--overloaded">
    <div class="illustration" role="img" aria-label="Illustration of a tired person leaning on a long scroll of virus information"></div>
    <div class="stat-bar"><div class="stat-fill" style="width:171px"></div><span class="stat-value">54%</span></div>
    <p class="stat-label">Feel overloaded by the<br>amount of information.</p>
  </section>

  <section class="band band--repetitive">
    <div class="illustration" role="img" aria-label="Illustration of a tired person beside a loop of repeating virus message bubbles"></div>
    <div class="stat-bar"><div class="stat-fill" style="width:171px"></div><span class="stat-value">51%</span></div>
    <p class="stat-label">Feel that the messages<br>are repetitive.</p>
  </section>

  <section class="band band--exaggerated">
    <div class="illustration" role="img" aria-label="Illustration of a tired person beside a chart with one curve rising higher than another"></div>
    <div class="stat-bar"><div class="stat-fill" style="width:147px"></div><span class="stat-value">47%</span></div>
    <p class="stat-label">Feel like messages<br>exaggerate how bad it is.</p>
  </section>

  <p class="summary">In other words, almost half of U.S. adults show signs of message fatigue, information overload, perceived message repetition, and perceived message exaggeration.</p>
</body>
</html>
```